Report template for evaluation reports to be used by non designers

We are looking for a report template that meets all the requirements listed in the attached documents. letter head, logo etc have been enclosed. Its important that the colour integrity is kept, but beyond that options are welcome.
Its important that the document is extremely easy to use and that is able to be adapted to include eatables, figures, pictures, text boxes etc and keep the integrity of the template

Target Market(s)

Governments, Civil society organisations and research institutions

Font styles to use
Sans Serif

Colors
6b449b
876aae
c0c0c0
000000

Requirements
Must have
• Clean, professional, not concluded, modern, must be easy to use
Should not have
• too busy, hard to use

```html
<!DOCTYPE html>
<html lang="en">
<head>
<meta charset="utf-8">
<title>Report Template Sheets</title>
<link href="https://fonts.googleapis.com/css2?family=Arimo:wght@400;700&family=Rubik:wght@500;700&display=swap" rel="stylesheet">
<style>
  :root {
    --brand: #56408a;
    --brand-line: #6b5aa6;
    --ink: #1a1a1a;
    --paper: #f7f7f5;
    --stage: #000000;
    --rule-grey: #c0c0c0;
  }
  * { margin: 0; padding: 0; box-sizing: border-box; }
  html, body { width: 905px; height: 1200px; overflow: hidden; background: var(--stage); }
  body { position: relative; font-family: "Arimo", Arial, sans-serif; color: var(--ink); }

  .sheet { position: absolute; width: 364px; height: 514px; background: var(--paper); overflow: hidden; }
  .sheet--cover { left: 74px; top: 64px; }
  .sheet--letterhead { left: 466px; top: 64px; }
  .sheet--index { left: 74px; top: 621px; }
  .sheet--content { left: 466px; top: 621px; }

  .brand-mark { position: absolute; font-family: "Arimo", Arial, sans-serif; font-weight: 400; color: var(--ink); text-align: center; line-height: 1; }
  .brand-mark__name { display: block; font-size: 21px; letter-spacing: 3px; }
  .brand-mark__sub { display: block; font-size: 4.4px; letter-spacing: 1.6px; margin-top: 5px; }

  .cover__band { position: absolute; left: 0; top: 0; width: 62px; height: 100%; background: var(--brand); }
  .cover__title { position: absolute; left: 62px; right: 0; top: 176px; text-align: center; font-family: "Rubik", Arial, sans-serif; font-weight: 500; color: var(--brand); font-size: 35px; line-height: 1.15; }
  .cover__author { position: absolute; left: 62px; right: 0; top: 270px; text-align: center; font-family: "Rubik", Arial, sans-serif; font-weight: 500; color: var(--brand); font-size: 16px; }
  .cover__date { position: absolute; left: 62px; right: 0; top: 293px; text-align: center; font-size: 10px; }

  .contact-block { position: absolute; font-size: 4.6px; line-height: 1; }
  .contact-block__row { display: flex; align-items: center; gap: 3px; height: 9px; white-space: nowrap; }
  .icon { display: inline-block; width: 5px; height: 5px; border: 0.8px solid var(--ink); border-radius: 50%; }
  .contact-block__rule { height: 0.8px; background: var(--brand-line); margin: 1px 0 3px; }
  .services { color: var(--brand); font-weight: 700; font-size: 4.6px; white-space: nowrap; }

  .index__heading { position: absolute; left: 34px; top: 80px; font-family: "Rubik", Arial, sans-serif; font-weight: 700; font-size: 15px; color: var(--brand); letter-spacing: 0.2px; }
  .index__rule { position: absolute; left: 34px; width: 296px; height: 1px; background: var(--brand-line); top: 103px; }
  .index__table { position: absolute; left: 34px; top: 108px; width: 296px; border-collapse: collapse; font-size: 4.8px; }
  .index__table th { font-weight: 400; text-align: left; height: 15px; vertical-align: middle; }
  .index__table td { height: 18.6px; border-bottom: 0.8px solid var(--brand-line); vertical-align: middle; }
  .index__table .col-no { width: 32px; text-align: center; }
  .index__table .col-topic { padding-left: 20px; }
  .index__table .col-page { width: 48px; padding-left: 14px; }
  .index__divider { position: absolute; top: 110px; width: 0.8px; height: 325px; background: var(--rule-grey); }

  .footer { position: absolute; left: 21px; right: 21px; top: 474px; font-size: 4.6px; }
  .footer__contacts { display: flex; align-items: center; gap: 3px; white-space: nowrap; justify-content: center; }
  .footer__rule { height: 0.8px; background: var(--brand-line); margin: 4px 0 6px; }
  .footer .services { text-align: center; font-weight: 700; }

  .content__author { position: absolute; left: 21px; top: 43px; font-family: "Rubik", Arial, sans-serif; font-weight: 700; color: var(--brand); font-size: 7.5px; }
  .content__date { position: absolute; left: 21px; top: 56px; font-size: 3px; font-weight: 700; }
  .content__rule { position: absolute; left: 21px; right: 21px; top: 68px; height: 0.8px; background: var(--brand-line); }
  .disclaimer { position: absolute; left: 22px; right: 22px; top: 435px; font-size: 3.3px; line-height: 1.3; color: #777; }
  .disclaimer__title { color: var(--brand); font-weight: 700; display: block; }
</style>
</head>
<body>

<section class="sheet sheet--cover">
  <div class="cover__band"></div>
  <div class="brand-mark" style="right:43px; top:27px;">
    <span class="brand-mark__name">CIVIC</span>
    <span class="brand-mark__sub">INSIGHT INSTITUTE</span>
  </div>
  <h1 class="cover__title">NAME<br>of the report</h1>
  <p class="cover__author">Anna Keller</p>
  <p class="cover__date">on 27th June 2018</p>
</section>

<section class="sheet sheet--letterhead">
  <div class="brand-mark" style="left:28px; top:27px;">
    <span class="brand-mark__name">CIVIC</span>
    <span class="brand-mark__sub">INSIGHT INSTITUTE</span>
  </div>
  <div class="contact-block" style="left:158px; top:26px;">
    <div class="contact-block__row"><span class="icon"></span>+41700000000 <span class="icon"></span>info@civicinsightinstitute.org</div>
    <div class="contact-block__row"><span class="icon"></span>civicinsightinstitute.org <span class="icon"></span>Registration Number: CHF-000.123.456</div>
    <div class="contact-block__rule"></div>
    <div class="services">Evaluation | Research | Policy Analysis | Capacity Development | Training</div>
  </div>
</section>

<section class="sheet sheet--index">
  <div class="brand-mark" style="left:40px; top:27px;">
    <span class="brand-mark__name">CIVIC</span>
    <span class="brand-mark__sub">INSIGHT INSTITUTE</span>
  </div>
  <h2 class="index__heading">EXAMPLE OF INDEX</h2>
  <div class="index__rule"></div>
  <div class="index__divider" style="left:66px;"></div>
  <div class="index__divider" style="left:282px;"></div>
  <table class="index__table">
    <thead><tr><th class="col-no" style="text-align:left">S.No.</th><th class="col-topic">TOPIC</th><th class="col-page">Page No.</th></tr></thead>
    <tbody>
      <tr><td class="col-no">1)</td><td class="col-topic">LOREM IPSUM</td><td class="col-page">1</td></tr>
      <tr><td class="col-no">2)</td><td class="col-topic">LOREM IPSUM</td><td class="col-page">2</td></tr>
      <tr><td class="col-no">3)</td><td class="col-topic">LOREM IPSUM</td><td class="col-page">3</td></tr>
      <tr><td class="col-no">4)</td><td class="col-topic">LOREM IPSUM</td><td class="col-page">4</td></tr>
      <tr><td class="col-no">5)</td><td class="col-topic">LOREM IPSUM</td><td class="col-page">5</td></tr>
      <tr><td class="col-no">6)</td><td class="col-topic">LOREM IPSUM</td><td class="col-page">6</td></tr>
      <tr><td class="col-no">7)</td><td class="col-topic">LOREM IPSUM</td><td class="col-page">7</td></tr>
      <tr><td class="col-no">8)</td><td class="col-topic">LOREM IPSUM</td><td class="col-page">8</td></tr>
      <tr><td class="col-no">9)</td><td class="col-topic">LOREM IPSUM</td><td class="col-page">9</td></tr>
      <tr><td class="col-no">10)</td><td class="col-topic">LOREM IPSUM</td><td class="col-page">10</td></tr>
      <tr><td class="col-no">11)</td><td class="col-topic">LOREM IPSUM</td><td class="col-page">11</td></tr>
      <tr><td class="col-no">12)</td><td class="col-topic">LOREM IPSUM</td><td class="col-page">12</td></tr>
      <tr><td class="col-no">13)</td><td class="col-topic">LOREM IPSUM</td><td class="col-page">13</td></tr>
      <tr><td class="col-no">14)</td><td class="col-topic">LOREM IPSUM</td><td class="col-page">14</td></tr>
    </tbody>
  </table>
  <footer class="footer">
    <div class="footer__contacts"><span class="icon"></span>+41700000000 <span class="icon"></span>info@civicinsightinstitute.org <span class="icon"></span>www.civicinsightinstitute.org <span class="icon"></span>Registration Number: CHF-000.123.456</div>
    <div class="footer__rule"></div>
    <div class="services">Evaluation &nbsp;| &nbsp;Research &nbsp;| &nbsp;Policy Analysis &nbsp;| &nbsp;Capacity Development &nbsp;| &nbsp;Training</div>
  </footer>
</section>

<section class="sheet sheet--content">
  <div class="brand-mark" style="right:40px; top:27px;">
    <span class="brand-mark__name">CIVIC</span>
    <span class="brand-mark__sub">INSIGHT INSTITUTE</span>
  </div>
  <p class="content__author">Lena Marsh</p>
  <p class="content__date">22nd June 2018</p>
  <div class="content__rule"></div>
  <p class="disclaimer"><span class="disclaimer__title">DISCLAIMER</span>This report is provided for general information only. Views expressed belong to the authors and do not necessarily reflect those of the institute or its partners. Data may be revised as new evidence becomes available. Readers should verify figures before citing them. No liability is accepted for decisions based on this content.</p>
  <footer class="footer">
    <div class="footer__contacts"><span class="icon"></span>+41700000000 <span class="icon"></span>info@civicinsightinstitute.org <span class="icon"></span>www.civicinsightinstitute.org <span class="icon"></span>Registration Number: CHF-000.123.456</div>
    <div class="footer__rule"></div>
    <div class="services">Evaluation &nbsp;| &nbsp;Research &nbsp;| &nbsp;Policy Analysis &nbsp;| &nbsp;Capacity Development &nbsp;| &nbsp;Training</div>
  </footer>
</section>

</body>
</html>
```